Jolly Blooms: Radiance Chews

We are seeking assistance with the packaging design for our new candy range of “Jolly Blooms” which is a range of heart shaped gummy candies.
The product we need help with is our RADIANCE CHEWS. Specifically, packaging design for the packaging (back side sealed bags) that will contain the candies (we can provide bag specs)
The candy is pink and heart shaped.
We’re wanting something brightly coloured and eye catching so it can be easily identified on shelves in stores.
In terms of colour scheme we want it to be feminine but fun. The candy has collagen and vitamin c in them and are targeted at females. We love pink, lavendar, yellow, orange, lime green etc. we’ve uploaded some inspo

```html
<!DOCTYPE html>
<html lang="en">
<head>
<meta charset="utf-8">
<title>Jolly Blooms Radiance Chews – Pack Front</title>
<link rel="stylesheet" href="https://fonts.googleapis.com/css2?family=Bebas+Neue&family=Londrina+Solid:wght@400;900&family=Allura&family=Oswald:wght@500&display=swap">
<style>
  :root {
    --backdrop: #f282a3;
    --bag: #e88aa6;
    --crimson: #cf2a5c;
    --crimson-deep: #b81f50;
    --white: #ffffff;
    --tag-text: #e0577f;
  }
  html, body {
    margin: 0;
    padding: 0;
    width: 1200px;
    height: 1200px;
    overflow: hidden;
    background: var(--backdrop);
  }
  .canvas { display: block; width: 1200px; height: 1200px; }
  .bag-body { fill: var(--bag); }
  .crimp-band { fill: var(--crimson); }
  .brand-name {
    font-family: "Londrina Solid", "Bebas Neue", sans-serif;
    font-weight: 900;
    font-size: 92px;
    letter-spacing: 4px;
    fill: var(--crimson);
  }
  .product-name {
    font-family: "Londrina Solid", sans-serif;
    font-weight: 400;
    font-size: 40px;
    letter-spacing: 3px;
    fill: var(--white);
  }
  .arc-dot { fill: var(--white); }
  .mascot-area { fill: url(#mascot-tone); }
  .flavour {
    font-family: "Bebas Neue", sans-serif;
    font-size: 46px;
    letter-spacing: 1px;
    fill: var(--crimson-deep);
  }
  .contains-label {
    font-family: "Allura", cursive;
    font-size: 36px;
    fill: var(--white);
  }
  .benefit-pill { fill: var(--crimson); }
  .benefit-divider { stroke: var(--white); stroke-width: 3; }
  .benefit-icon { fill: none; stroke: var(--white); stroke-width: 2.5; stroke-linejoin: round; stroke-linecap: round; }
  .benefit-label {
    font-family: "Bebas Neue", sans-serif;
    font-size: 27px;
    letter-spacing: .5px;
    fill: var(--white);
  }
  .icon-letter {
    font-family: "Bebas Neue", sans-serif;
    font-size: 18px;
    fill: var(--white);
  }
  .weight-heart { fill: var(--white); }
  .weight-text {
    font-family: "Oswald", sans-serif;
    font-weight: 500;
    font-size: 34px;
    fill: var(--tag-text);
  }
</style>
</head>
<body>
<svg class="canvas" viewBox="0 0 1200 1200" xmlns="http://www.w3.org/2000/svg">
  <defs>
    <path id="brand-arc" d="M270 540 A340 340 0 0 1 930 540"/>
    <path id="product-arc" d="M360 640 A240 240 0 0 1 840 640"/>
    <radialGradient id="mascot-tone" cx="50%" cy="45%" r="60%">
      <stop offset="0%" stop-color="#d12e60"/>
      <stop offset="65%" stop-color="#d9497a"/>
      <stop offset="100%" stop-color="#e88aa6"/>
    </radialGradient>
  </defs>

  <g class="pack">
    <rect class="bag-body" x="250" y="120" width="700" height="960"/>
    <rect class="crimp-band" x="250" y="120" width="700" height="58" role="img" aria-label="Crimped top seal with small heart pattern"/>
    <rect class="crimp-band" x="250" y="1022" width="700" height="58" role="img" aria-label="Crimped bottom seal with small heart pattern"/>

    <g class="brand-lockup">
      <text class="brand-name"><textPath href="#brand-arc" startOffset="50%" text-anchor="middle">JOLLY BLOOMS</textPath></text>
      <text class="product-name"><textPath href="#product-arc" startOffset="50%" text-anchor="middle">RADIANCE CHEWS</textPath></text>
      <circle class="arc-dot" cx="412" cy="488" r="5"/>
      <circle class="arc-dot" cx="788" cy="488" r="5"/>
    </g>

    <rect class="mascot-area" x="425" y="440" width="350" height="310" rx="40" role="img" aria-label="Illustration: large pink heart candy character inside a dashed heart outline, surrounded by small hearts"/>

    <text class="flavour" x="600" y="800" text-anchor="middle">PINK LEMONADE FLAVOUR</text>

    <g class="benefits">
      <rect class="benefit-pill" x="440" y="830" width="320" height="115" rx="50"/>
      <line class="benefit-divider" x1="600" y1="852" x2="600" y2="922"/>
      <g class="benefit-icon">
        <polygon points="510,844 520,850 520,862 510,868 500,862 500,850"/>
        <polygon points="530,844 540,850 540,862 530,868 520,862 520,850"/>
        <polygon points="520,862 530,868 530,880 520,886 510,880 510,868"/>
        <path d="M694 842 C694 842 677 862 677 873 A17 17 0 0 0 711 873 C711 862 694 842 694 842 Z"/>
      </g>
      <text class="icon-letter" x="694" y="882" text-anchor="middle">C</text>
      <text class="benefit-label" x="520" y="926" text-anchor="middle">COLLAGEN</text>
      <text class="benefit-label" x="694" y="926" text-anchor="middle">VITAMIN C</text>
      <text class="contains-label" x="510" y="836">Contains</text>
    </g>

    <g class="net-weight">
      <path class="weight-heart" d="M880 985 C840 955 825 935 825 912 C825 890 845 876 862 880 C872 882 878 890 880 896 C882 890 888 882 898 880 C915 876 935 890 935 912 C935 935 920 955 880 985 Z"/>
      <text class="weight-text" x="880" y="935" text-anchor="middle">50g</text>
    </g>
  </g>
</svg>
</body>
</html>
```